Print design needed to improve the layout and look of some existing documents

We need someone to take a couple of existing documents that we have and make them look much better using our existing logo and corporate colors etc. We require these to be delivered in a format that will allow our staff to edit the content as necessary via Microsoft word for conversion once finalized into a PDF. Ideally, we will also be able to use this as a newsletter template or for other documents that might be required in our business. www.calderfinch.com.au
Updates

Project Deadline Extended Reason: So far, I have only seen one design that I believe is quite good quality. Added Sunday, July 3, 2016

Target Market(s)

Business owners, executives, retirees

Industry/Entity Type

Financial Service

Font styles to use
Serif

Requirements
Must have
• Design that uses our existing branding and colors. It also needs to be ina form that we can edit the content / update easily. Ideally the format / layout could also be used for other documents such as short newsletters etc.
Nice to have
• Fresh, simple and crisp. Very professional looking.
Should not have
• strange fonts, weird layouts.

```html
<!DOCTYPE html>
<html lang="en">
<head>
<meta charset="utf-8">
<title>Calder Finch – Privacy Policy Layout Options</title>
<link href="https://fonts.googleapis.com/css2?family=Raleway:wght@300;400;600;700;800&display=swap" rel="stylesheet">
<style>
:root{
  --bg:#ece8e2;
  --ink:#4d4f52;
  --muted:#8a8c90;
  --accent:#1c8ec4;
  --band:#58595b;
  --sheet-grey:#e2e3e5;
  --panel:#eef1e1;
  --green:#6fae45;
  --blue-a:#1f72b8;
  --blue-b:#3aa0dc;
}
*{box-sizing:border-box;margin:0;padding:0}
html,body{width:1200px;height:1200px;overflow:hidden;background:var(--bg);font-family:"Raleway",sans-serif;color:var(--ink)}
.board{position:relative;width:1200px;height:1200px}
.option-label{position:absolute;top:44px;width:348px;text-align:center;font-size:52px;font-weight:800;color:#3b3c3e;letter-spacing:-.5px}
.page{position:absolute;width:348px;height:490px;background:#fff;overflow:hidden;box-shadow:0 2px 8px rgba(0,0,0,.18)}
.col-1{left:40px}.col-2{left:426px}.col-3{left:812px}
.row-1{top:144px}.row-2{top:656px}

/* shared type */
.brand{display:flex;align-items:center;gap:6px}
.brand-mark{width:9px;height:9px;background:var(--accent)}
.brand-name{font-size:15px;font-weight:400;letter-spacing:.5px;color:var(--ink)}
.brand-sub{font-size:3.4px;letter-spacing:4px;color:var(--ink);margin-top:1px}
.doc-title{font-size:10px;font-weight:700;color:var(--accent);letter-spacing:.2px}
.cols{display:flex;gap:10px}
.cols>div{flex:1;min-width:0}
h3{font-size:6.2px;font-weight:700;color:var(--accent);line-height:1.3;margin:7px 0 4px}
p,li{font-size:4.4px;line-height:1.6;color:var(--muted);margin-bottom:5px}
ul{list-style:none;margin:0 0 5px 6px}
li{margin-bottom:1px}
li::before{content:"– "}
p.lead-in{color:var(--accent);font-weight:600}
.tagline{font-size:4.6px;color:var(--green)}

/* option 1 */
.opt1{padding:9px}
.opt1 .sheet{position:relative;background:var(--sheet-grey);height:100%;padding:14px 12px 0}
.opt1 .doc-title{margin:27px 0 5px}
.opt1 h3{color:var(--accent);border-top:2px solid var(--accent);padding-top:3px;margin-top:8px}
.opt1 .body{height:328px;overflow:hidden}
.opt1.second .body{height:388px}
.opt1 h3.head-h3{margin-top:30px}
.footer-band{position:absolute;left:12px;right:12px;bottom:10px;background:var(--band);color:#fff;padding:5px 6px}
.footer-band .co{font-size:4.6px;margin-bottom:2px}
.footer-band .contact{font-size:3.3px;display:flex;gap:8px;opacity:.9}

/* header band (options 2 & 3) */
.head-band{height:52px;background:var(--band);display:flex;justify-content:space-between;align-items:center;padding:0 10px 0 12px}
.head-band .brand-name,.head-band .brand-sub{color:#fff}
.head-contact{font-size:4.2px;color:#fff;line-height:1.55}
.head-contact .co{font-size:4.6px}
.head-contact span{display:block;font-size:3.6px}
.content{padding:11px 20px 0}
.content .doc-title{margin-bottom:7px}
.content .body{height:375px;overflow:hidden}
.panel{background:var(--panel);padding:1px 6px 4px}
.panel h3{color:#3e4043}
.opt2 h3,.opt3 h3{color:#3e4043}
.panel .green-h{color:var(--green)}
.page-foot{position:absolute;left:20px;bottom:18px}

/* option 3 extras */
.opt3 .footer-band{left:12px;right:12px;bottom:32px}
.blue-band{height:28px;background:linear-gradient(90deg,var(--blue-a),var(--blue-b))}
.green-band{position:absolute;left:10px;right:10px;bottom:18px;height:11px;background:var(--green);padding:3px 10px}
.green-band .tagline{color:#fff;font-size:4.4px}
.opt3 .content .body{height:360px}
.opt3.second .content{padding-top:16px}
.opt3.second .content .body{height:410px}
.opt3 .content .body.first{height:355px}
</style>
</head>
<body>
<main class="board">

<div class="option-label col-1">Option1</div>
<div class="option-label col-2">Option2</div>
<div class="option-label col-3">Option3</div>

<!-- ===== Option 1, page 1 ===== -->
<section class="page opt1 col-1 row-1">
  <div class="sheet">
    <div class="brand"><span class="brand-mark"></span><div><div class="brand-name">CALDER FINCH</div><div class="brand-sub">PRIVATE WEALTH</div></div></div>
    <h1 class="doc-title">CALDER FINCH PTY LTD PRIVACY POLICY</h1>
    <div class="body">
      <p>We are committed to protecting your privacy in accordance with the Privacy Act 1988 (Cth). This Policy describes our current policies and practices in relation to the collection, handling, use and disclosure of personal information. It also deals with how you can complain about a breach of the privacy laws, how you can access the personal information we hold about you and how to have that information corrected.</p>
      <div class="cols">
        <div>
          <h3>What information do we collect and how do we use it?</h3>
          <p>If you are acquiring or have acquired a service from Calder Finch Pty Ltd, we collect and hold your personal information for the purpose of providing you with relevant and accurate service and financial advice as well as managing and administering the service. This can include a broad range of information ranging from your name, postal and email address, date of birth, contact details and age to other information about your personal affairs including your financial details, tax file numbers or other information the organisation considers necessary.</p>
          <p>We may disclose the information that you provide to third party organisations where you have request that we liaise with or refer you to the organisations. This may include firms providing accounting, legal, credit, transactional banking, investment administration or insurance services.</p>
          <p>We may use your information to enable us to manage your ongoing requirements and our relationship with you. We may do so by mail or electronically unless you tell us that you do not wish to receive electronic communications.</p>
          <p>From time to time we may use your contact details to send you offers, updates, events, articles, newsletters or other information about services or events that we believe will be of interest to you. You can contact us at any time if you no longer wish us to do so.</p>
          <p>We may also use your information internally to help us improve our services and help resolve any problems.</p>
        </div>
        <div>
          <h3>What if you don't provide some information to us?</h3>
          <p>If you do not provide us with some or all of the information that we ask for, we may not be able to accurately assess your situation and provide relevant and accurate financial advice.</p>
          <h3>How do we hold and protect your information?</h3>
          <p>We strive to maintain the relevance, reliability, accuracy, completeness and currency of the personal information we hold and to protect its privacy and security. We keep personal information only for as long as is reasonably necessary for the purpose for which it was collected or to comply with any applicable legal or ethical reporting or document retention requirements.</p>
          <p>We store information collected from you in different ways, including in paper and electronic form. The security of your personal information is important to us and we take reasonable steps to protect it from misuse and loss and unauthorised access, modification or disclosure.</p>
          <p>Some of the ways we ensure that your information is safe are:</p>
          <ul><li>confidentiality requirements for our employees</li><li>security measures for systems access</li><li>access control for our building</li></ul>
          <p>We also maintain physical security over our paper and electronic data and premises, by using locked and security systems.</p>
        </div>
      </div>
    </div>
    <footer class="footer-band">
      <div class="co">Calder Finch Pty Ltd | AFSL 500123 | ABN 12 345 678 901</div>
      <div class="contact"><span>⌂ 12 Marlowe Lane, Brookvale, WA 6148</span><span>✉ PO Box 204, Harbour Point, WA 6148</span><span>www.calderfinch.com.au</span><span>☎ 08 6100 2040</span></div>
    </footer>
  </div>
</section>

<!-- ===== Option 1, page 2 ===== -->
<section class="page opt1 second col-1 row-2">
  <div class="sheet">
    <div class="brand"><span class="brand-mark"></span><div><div class="brand-name">CALDER FINCH</div><div class="brand-sub">PRIVATE WEALTH</div></div></div>
    <div class="body">
      <div class="cols">
        <div>
          <h3 class="head-h3">Will we disclose the information we collect to anyone?</h3>
          <p>We do not sell, trade, or rent your personal information to others. We may disclose your information to third party organisations where you have request that we liaise with or refer you to the organisations. This may include firms providing investment, superannuation, accounting, legal, credit, transactional banking or insurance services and may need to provide your information to contractors who supply services to us or to other companies in the event of a corporate sale, merger, reorganisation, dissolution or similar event. However, we will take all reasonable steps to ensure that they protect your information in the same way that we do.</p>
          <p>We may also provide your information to others if we are required to do so by law or under some unusual other circumstances which the Privacy Act permits. We will not provide your information to any overseas recipients unless we are required to by Law.</p>
          <h3>How can you check, update or change the information we are holding?</h3>
          <p>Upon receipt of your written request and enough information to allow us to identify the information, we will disclose to you the personal information we hold about you. We will also correct, amend or delete any personal information that we agree is inaccurate, irrelevant, out of date or incomplete.</p>
          <p>If you wish to access or correct your personal information please contact our office (see contact details below). We do not charge for receiving a request for access to personal information or for complying with a correction request.</p>
          <p>In some limited cases, we may need to refuse access to your information or refuse a request for correction. We will advise you as soon as possible after your request if this is the case and the reasons for our refusal.</p>
        </div>
        <div>
          <h3 class="head-h3">What happens if you want to complain?</h3>
          <p>If you have any concerns about whether we have complied with the Privacy Act or this Privacy Policy when collecting or handling your personal information, you can call us on 08 6100 2040 or email your concerns to admin@calderfinch.com.au</p>
          <p>We will consider any privacy related complaint through our internal complaints resolution process and we will try to respond with a decision within 45 days of you making the complaint.</p>
          <h3>Your consent</h3>
          <p>By asking us to assist with your financial needs, you consent to the collection and use of the information you have provided to us for the purposes described above.</p>
          <h3>Tell us what you think</h3>
          <p>We welcome your questions and comments about privacy. If you have any concerns or complaints, please contact us on 08 6100 2040 or via email on admin@calderfinch.com.au</p>
          <p class="lead-in">Privacy Policy Statement – V2015</p>
        </div>
      </div>
    </div>
    <footer class="footer-band">
      <div class="co">Calder Finch Pty Ltd | AFSL 500123 | ABN 12 345 678 901</div>
      <div class="contact"><span>⌂ 12 Marlowe Lane, Brookvale, WA 6148</span><span>✉ PO Box 204, Harbour Point, WA 6148</span><span>www.calderfinch.com.au</span><span>☎ 08 6100 2040</span></div>
    </footer>
  </div>
</section>

<!-- ===== Option 2, page 1 ===== -->
<section class="page opt2 col-2 row-1">
  <header class="head-band">
    <div class="brand"><span class="brand-mark"></span><div><div class="brand-name">CALDER FINCH</div><div class="brand-sub">PRIVATE WEALTH</div></div></div>
    <div class="head-contact"><div class="co">Calder Finch Pty Ltd | AFSL 500123 | ABN 12 345 678 901</div><span>⌂ 12 Marlowe Lane, Brookvale, WA 6148</span><span>✉ PO Box 204, Harbour Point, WA 6148</span><span>www.calderfinch.com.au | ☎ 08 6100 2040</span></div>
  </header>
  <div class="content">
    <h1 class="doc-title">CALDER FINCH PTY LTD PRIVACY POLICY</h1>
    <div class="body cols">
      <div>
        <p>We are committed to protecting your privacy in accordance with the Privacy Act 1988 (Cth). This Policy describes our current policies and practices in relation to the collection, handling, use and disclosure of personal information. It also deals with how you can complain about a breach of the privacy laws, how you can access the personal information we hold about you and how to have that information corrected.</p>
        <h3>What information do we collect and how do we use it?</h3>
        <p>If you are acquiring or have acquired a service from Calder Finch Pty Ltd, we collect and hold your personal information for the purpose of providing you with relevant and accurate service and financial advice as well as managing and administering the service. This can include a broad range of information ranging from your name, postal and email address, date of birth, contact details and age to other information about your personal affairs including your financial details, tax file numbers or other information the organisation considers necessary.</p>
        <p>We may disclose the information that you provide to third party organisations where you have request that we liaise with or refer you to the organisations. This may include firms providing accounting, legal, credit, transactional banking, investment administration or insurance services.</p>
        <p>We may use your information to enable us to manage your ongoing requirements and our relationship with you. We may do so by mail or electronically unless you tell us that you do not wish to receive electronic communications.</p>
        <p>From time to time we may use your contact details to send you offers, updates, events, articles, newsletters or other information about services or events that we believe will be of interest to you. You can contact us at any time if you no longer wish us to do so.</p>
        <p>We may also use your information internally to help us improve our services and help resolve any problems.</p>
      </div>
      <div>
        <h3 style="margin-top:0">What if you don't provide some information to us?</h3>
        <p>If you do not provide us with some or all of the information that we ask for, we may not be able to accurately assess your situation and provide relevant and accurate financial advice.</p>
        <div class="panel">
          <h3>How do we hold and protect your information?</h3>
          <p>We strive to maintain the relevance, reliability, accuracy, completeness and currency of the personal information we hold and to protect its privacy and security. We keep personal information only for as long as is reasonably necessary for the purpose for which it was collected or to comply with any applicable legal or ethical reporting or document retention requirements.</p>
          <p>We store information collected from you in different ways, including in paper and electronic form. The security of your personal information is important to us and we take reasonable steps to protect it from misuse and loss and unauthorised access, modification or disclosure.</p>
          <p class="lead-in">Some of the ways we ensure that your information is safe are:</p>
          <ul><li>confidentiality requirements for our employees</li><li>security measures for systems access</li><li>access control for our building</li></ul>
          <p>We also maintain physical security over our paper and electronic data and premises, by using locked and security systems.</p>
        </div>
        <h3>Will we disclose the information we collect to anyone?</h3>
        <p>We do not sell, trade, or rent your personal information to others. We may disclose your information to third party organisations where you have request that we</p>
      </div>
    </div>
  </div>
</section>

<!-- ===== Option 2, page 2 ===== -->
<section class="page opt2 col-2 row-2">
  <header class="head-band">
    <div class="brand"><span class="brand-mark"></span><div><div class="brand-name">CALDER FINCH</div><div class="brand-sub">PRIVATE WEALTH</div></div></div>
    <div class="head-contact"><div class="co">Calder Finch Pty Ltd | AFSL 500123 | ABN 12 345 678 901</div><span>⌂ 12 Marlowe Lane, Brookvale, WA 6148</span><span>✉ PO Box 204, Harbour Point, WA 6148</span><span>www.calderfinch.com.au | ☎ 08 6100 2040</span></div>
  </header>
  <div class="content">
    <div class="body cols">
      <div>
        <p>liaise with or refer you to the organisations. This may include firms providing investment, superannuation, accounting, legal, credit, transactional banking or insurance services and may need to provide your information to contractors who supply services to us or to other companies in the event of a corporate sale, merger, reorganisation, dissolution or similar event. However, we will take all reasonable steps to ensure that they protect your information in the same way that we do.</p>
        <p>We may also provide your information to others if we are required to do so by law or under some unusual other circumstances which the Privacy Act permits. We will not provide your information to any overseas recipients unless we are required to by Law.</p>
        <h3>How can you check, update or change the information we are holding?</h3>
        <p>Upon receipt of your written request and enough information to allow us to identify the information, we will disclose to you the personal information we hold about you. We will also correct, amend or delete any personal information that we agree is inaccurate, irrelevant, out of date or incomplete.</p>
        <p>If you wish to access or correct your personal information please contact our office (see contact details below). We do not charge for receiving a request for access to personal information or for complying with a correction request.</p>
      </div>
      <div>
        <p>In some limited cases, we may need to refuse access to your information or refuse a request for correction. We will advise you as soon as possible after your request if this is the case and the reasons for our refusal.</p>
        <h3>What happens if you want to complain?</h3>
        <p>If you have any concerns about whether we have complied with the Privacy Act or this Privacy Policy when collecting or handling your personal information, you can call us on 08 6100 2040 or email your concerns to admin@calderfinch.com.au</p>
        <p>We will consider any privacy related complaint through our internal complaints resolution process and we will try to respond with a decision within 45 days of you making the complaint.</p>
        <p>By asking us to assist with your financial needs, you consent to the collection and use of the information you have provided to us for the purposes described above.</p>
        <div class="panel">
          <h3 class="green-h">Tell us what you think</h3>
          <p>We welcome your questions and comments about privacy. If you have any concerns or complaints, please contact us on 08 6100 2040 or via email on admin@calderfinch.com.au</p>
        </div>
      </div>
    </div>
  </div>
  <div class="page-foot tagline">Privacy Policy Statement – V2015</div>
</section>

<!-- ===== Option 3, page 1 ===== -->
<section class="page opt3 col-3 row-1">
  <header class="head-band">
    <div class="brand"><span class="brand-mark"></span><div><div class="brand-name">CALDER FINCH</div><div class="brand-sub">PRIVATE WEALTH</div></div></div>
  </header>
  <div class="content">
    <h1 class="doc-title">CALDER FINCH PTY LTD PRIVACY POLICY</h1>
    <div class="body first cols">
      <div>
        <p>We are committed to protecting your privacy in accordance with the Privacy Act 1988 (Cth). This Policy describes our current policies and practices in relation to the collection, handling, use and disclosure of personal information. It also deals with how you can complain about a breach of the privacy laws, how you can access the personal information we hold about you and how to have that information corrected.</p>
        <h3>What information do we collect and how do we use it?</h3>
        <p>If you are acquiring or have acquired a service from Calder Finch Pty Ltd, we collect and hold your personal information for the purpose of providing you with relevant and accurate service and financial advice as well as managing and administering the service. This can include a broad range of information ranging from your name, postal and email address, date of birth, contact details and age to other information about your personal affairs including your financial details, tax file numbers or other information the organisation considers necessary.</p>
        <p>We may disclose the information that you provide to third party organisations where you have request that we liaise with or refer you to the organisations. This may include firms providing accounting, legal, credit, transactional banking, investment administration or insurance services.</p>
        <p>We may use your information to enable us to manage your ongoing requirements and our relationship with you. We may do so by mail or electronically unless you tell us that you do not wish to receive electronic communications.</p>
        <p>From time to time we may use your contact details to send you offers, updates, events, articles, newsletters or other information about services or events that we believe will be of interest to you. You can contact us at any time if you no longer wish us to do so.</p>
      </div>
      <div>
        <p>We may also use your information internally to help us improve our services and help resolve any problems.</p>
        <h3>What if you don't provide some information to us?</h3>
        <p>If you do not provide us with some or all of the information that we ask for, we may not be able to accurately assess your situation and provide relevant and accurate financial advice.</p>
        <div class="panel">
          <h3>How do we hold and protect your information?</h3>
          <p>We strive to maintain the relevance, reliability, accuracy, completeness and currency of the personal information we hold and to protect its privacy and security. We keep personal information only for as long as is reasonably necessary for the purpose for which it was collected or to comply with any applicable legal or ethical reporting or document retention requirements.</p>
          <p>We store information collected from you in different ways, including in paper and electronic form. The security of your personal information is important to us and we take reasonable steps to protect it from misuse and loss and unauthorised access, modification or disclosure.</p>
          <p class="lead-in">Some of the ways we ensure that your information is safe are:</p>
          <ul><li>confidentiality requirements for our employees</li><li>security measures for systems access</li><li>access control for our building</li></ul>
          <p>We also maintain physical security over our paper and electronic data and premises, by using locked and security systems.</p>
        </div>
      </div>
    </div>
  </div>
  <footer class="footer-band">
    <div class="co">Calder Finch Pty Ltd | AFSL 500123 | ABN 12 345 678 901</div>
    <div class="contact"><span>⌂ 12 Marlowe Lane, Brookvale, WA 6148</span><span>✉ PO Box 204, Harbour Point, WA 6148</span></div>
    <div class="contact"><span>www.calderfinch.com.au</span><span>☎ 08 6100 2040</span></div>
  </footer>
</section>

<!-- ===== Option 3, page 2 ===== -->
<section class="page opt3 second col-3 row-2">
  <div class="blue-band"></div>
  <div class="content">
    <div class="body cols">
      <div>
        <h3 style="margin-top:0">Will we disclose the information we collect to anyone?</h3>
        <p>We do not sell, trade, or rent your personal information to others. We may disclose your information to third party organisations where you have request that we liaise with or refer you to the organisations. This may include firms providing investment, superannuation, accounting, legal, credit, transactional banking or insurance services and may need to provide your information to contractors who supply services to us or to other companies in the event of a corporate sale, merger, reorganisation, dissolution or similar event. However, we will take all reasonable steps to ensure that they protect your information in the same way that we do.</p>
        <p>We may also provide your information to others if we are required to do so by law or under some unusual other circumstances which the Privacy Act permits. We will not provide your information to any overseas recipients unless we are required to by Law.</p>
        <h3>How can you check, update or change the information we are holding?</h3>
        <p>Upon receipt of your written request and enough information to allow us to identify the information, we will disclose to you the personal information we hold about you. We will also correct, amend or delete any personal information that we agree is inaccurate, irrelevant, out of date or incomplete.</p>
      </div>
      <div>
        <p>If you wish to access or correct your personal information please contact our office (see contact details below). We do not charge for receiving a request for access to personal information or for complying with a correction request.</p>
        <p>In some limited cases, we may need to refuse access to your information or refuse a request for correction. We will advise you as soon as possible after your request if this is the case and the reasons for our refusal.</p>
        <h3>What happens if you want to complain?</h3>
        <p>If you have any concerns about whether we have complied with the Privacy Act or this Privacy Policy when collecting or handling your personal information, you can call us on 08 6100 2040 or email your concerns to admin@calderfinch.com.au</p>
        <p>We will consider any privacy related complaint through our internal complaints resolution process and we will try to respond with a decision within 45 days of you making the complaint.</p>
        <p>By asking us to assist with your financial needs, you consent to the collection and use of the information you have provided to us for the purposes described above.</p>
        <div class="panel">
          <h3 class="green-h">Tell us what you think</h3>
          <p>We welcome your questions and comments about privacy. If you have any concerns or complaints, please contact us on 08 6100 2040 or via email on admin@calderfinch.com.au</p>
        </div>
      </div>
    </div>
  </div>
  <div class="green-band"><span class="tagline">Privacy Policy Statement – V2015</span></div>
</section>

</main>
</body>
</html>
```